Slick Quillnest Ad

We've recently re-branded our business to reflect our ethos "Wealth is about more than money - it's about choice." We aim to protect your hard-earned success and help achieve your lifestyle aspirations, whether that's retiring at fifty to go globetrotting, or buying your first home. We're a financial consultancy that primarily services high-net-worth clients.

Our brand is minimalist, modern (check out our website) and the brief focuses on our strong investment return for the past 12 years.

Task: The attached brief is for a Quillnest advertisement. Please see competitor images as a guide to how 'returns' and 'branding' can both be displayed in a design.

Target Market(s)

+30

Font styles to use
Sans Serif

Requirements
Must have
• Creative should feature the strong investment return, and design aesthetic should be 'on-brand' (modern, minimalist, lifestyle focused).

```html
<!DOCTYPE html>
<html lang="en">
<head>
<meta charset="UTF-8">
<title>Quillnest — Investment Returns Ad</title>
<link href="https://fonts.googleapis.com/css2?family=Mulish:wght@400;600;800&display=swap" rel="stylesheet">
<style>
  :root {
    --page-bg: #ffffff;
    --card-bg: #fafafa;
    --olive: #a4ad12;
    --ink: #3c3d3f;
    --line-left: #b1b385;
    --line-right: #d5da86;
    --glass-light: #eef3f4;
    --glass-mid: #d3e0e2;
    --glass-deep: #b9cdd1;
  }
  * { margin: 0; padding: 0; box-sizing: border-box; }
  html, body {
    width: 1200px;
    height: 1000px;
    overflow: hidden;
    background: var(--page-bg);
    font-family: "Mulish", Arial, sans-serif;
  }
  .ad {
    position: absolute;
    left: 90px;
    top: 233px;
    width: 1020px;
    height: 534px;
    background: var(--card-bg);
    overflow: hidden;
    box-shadow: 0 1px 4px rgba(0,0,0,0.12);
  }
  .architecture {
    position: absolute;
    left: 430px;
    top: 0;
    width: 590px;
    height: 534px;
    background:
      repeating-linear-gradient(90deg, rgba(255,255,255,0.0) 0 26px, rgba(255,255,255,0.75) 26px 40px, rgba(185,205,209,0.35) 40px 52px),
      linear-gradient(90deg, rgba(250,250,250,1) 0%, var(--glass-light) 25%, var(--glass-mid) 70%, var(--glass-deep) 100%);
    clip-path: polygon(20% 100%, 55% 20%, 68% 0, 100% 0, 100% 100%);
  }
  .architecture-corner {
    position: absolute;
    left: 0;
    top: 385px;
    width: 180px;
    height: 149px;
    background: linear-gradient(160deg, #eef1f2 0%, #e2e7e9 100%);
    clip-path: polygon(0 0, 100% 100%, 0 100%);
  }
  .return-chart {
    position: absolute;
    left: 0;
    top: 0;
    width: 1020px;
    height: 534px;
  }
  .headline {
    position: absolute;
    left: 42px;
    top: 45px;
    color: var(--ink);
  }
  .headline-lead {
    font-size: 21px;
    font-weight: 400;
    line-height: 26px;
  }
  .headline-figure {
    font-size: 48.5px;
    font-weight: 800;
    color: var(--olive);
    line-height: 48px;
    letter-spacing: 0.4px;
  }
  .headline-period {
    font-size: 20.5px;
    font-weight: 600;
    line-height: 22px;
  }
  .brand {
    position: absolute;
    left: 42px;
    top: 162px;
    display: flex;
    align-items: center;
    gap: 10px;
    color: var(--olive);
  }
  .brand-dot {
    width: 30px;
    height: 30px;
    border-radius: 50%;
    border: 2px solid var(--olive);
  }
  .brand-name {
    font-size: 24px;
    font-weight: 800;
  }
</style>
</head>
<body>
  <section class="ad">
    <div class="architecture" role="img" aria-label="Photograph of a modern white glass building facade with angled steel fins"></div>
    <div class="architecture-corner" role="img" aria-label="Photograph of white architectural panels"></div>

    <svg class="return-chart" viewBox="0 0 1020 534" aria-hidden="true">
      <defs>
        <linearGradient id="chartStroke" x1="0" y1="0" x2="660" y2="0" gradientUnits="userSpaceOnUse">
          <stop offset="0" stop-color="var(--line-left)"/>
          <stop offset="0.5" stop-color="var(--line-left)"/>
          <stop offset="0.62" stop-color="var(--line-right)"/>
          <stop offset="1" stop-color="var(--line-right)"/>
        </linearGradient>
      </defs>
      <polyline fill="none" stroke="url(#chartStroke)" stroke-width="3.5" stroke-linejoin="round"
        points="0,360 28,372 55,348 84,398 112,380 140,430 170,412 200,452 232,436 262,468 294,450 324,474 356,446 388,458 418,420 446,398 474,408 500,350 528,330 552,356 578,290 604,250 628,262 648,160 672,120 700,60 720,0"/>
    </svg>

    <div class="headline">
      <p class="headline-lead">Our global investment portfolio delivered</p>
      <p class="headline-figure">20.5% RETURNS</p>
      <p class="headline-period">over the past 12 months</p>
    </div>

    <div class="brand">
      <span class="brand-dot"></span>
      <span class="brand-name">Quillnest</span>
    </div>
  </section>
</body>
</html>
```